THE TALL COPPER ATLAS OF PORTS

subtitle: AN INTRO TO SEARCH ENGINE OPTIMIZATION
background: white
dimensions: 1562x2500

Target Market(s)

Marketing professionals

Industry/Entity Type

Digital Marketing

Font styles to use
Sans Serif

Colors
ffffff
1b1b1b
3176b5

Requirements
Should not have
• Images or graphics

```html
<!DOCTYPE html>
<html lang="en">
<head>
<meta charset="utf-8">
<title>The Tall Copper Atlas of Ports — Cover</title>
<link rel="stylesheet" href="https://fonts.googleapis.com/css2?family=Open+Sans:wght@700;800&display=swap">
<style>
  :root {
    --stage: #d6d6d6;
    --paper: #ffffff;
    --ink: #1b1b1b;
    --brand-blue: #3176b5;
    --band-light: #2a97d0;
    --band-deep: #3a78b6;
    --fold: #2c6698;
  }
  html, body {
    margin: 0;
    width: 1200px;
    height: 978px;
    overflow: hidden;
    background: var(--stage);
  }
  .stage {
    position: relative;
    width: 1200px;
    height: 978px;
  }
  .cover {
    position: absolute;
    left: 319px;
    top: 39px;
    width: 562px;
    height: 900px;
    background: var(--paper);
    box-shadow: 0 6px 24px rgba(27, 27, 27, 0.18);
  }
  .cover svg { display: block; }
  .subtitle {
    font-family: "Open Sans", sans-serif;
    font-weight: 700;
    font-size: 62px;
    fill: var(--brand-blue);
    letter-spacing: 1px;
  }
  .title-word {
    font-family: "Open Sans", sans-serif;
    font-weight: 800;
    font-size: 190px;
    fill: var(--paper);
  }
  .band { fill: url(#bandShade); }
  .fold { fill: var(--fold); opacity: 0.9; }
</style>
</head>
<body>
<main class="stage">
  <article class="cover">
    <svg viewBox="0 0 1562 2500" width="562" height="900" aria-labelledby="cover-title">
      <title id="cover-title">The Tall Copper Atlas of Ports — An intro to search engine optimization</title>
      <defs>
        <clipPath id="coverClip"><rect width="1562" height="2500"/></clipPath>
        <linearGradient id="bandShade" x1="0" y1="0" x2="1" y2="0">
          <stop offset="0" stop-color="var(--band-light)"/>
          <stop offset="1" stop-color="var(--band-deep)"/>
        </linearGradient>
      </defs>
      <rect class="cover-paper" width="1562" height="2500" fill="var(--paper)"/>
      <g clip-path="url(#coverClip)">
        <g class="ribbon" transform="translate(0 950) rotate(-27)">
          <text class="subtitle" x="60" y="-40">AN INTRO TO SEARCH ENGINE OPTIMIZATION</text>

          <!-- folds joining each band to the next -->
          <polygon class="fold" points="1600,250 1320,250 -300,330 -20,330"/>
          <polygon class="fold" points="1420,580 1140,580 -450,660 -170,660"/>
          <polygon class="fold" points="1280,910 1000,910 -600,990 -320,990"/>

          <rect class="band" x="-900" y="0" width="2500" height="250"/>
          <rect class="band" x="-900" y="330" width="2320" height="250"/>
          <rect class="band" x="-900" y="660" width="2180" height="250"/>
          <rect class="band" x="-900" y="990" width="2020" height="250"/>

          <text class="title-word" x="1540" y="193" text-anchor="end">THE TALL</text>
          <text class="title-word" x="1360" y="523" text-anchor="end">COPPER</text>
          <text class="title-word" x="1220" y="853" text-anchor="end">ATLAS</text>
          <text class="title-word" x="1060" y="1183" text-anchor="end">OF PORTS</text>
        </g>
      </g>
    </svg>
  </article>
</main>
</body>
</html>
```